Need a cover for eBook:
Title is: 47 Blunders That Sink Your Indie-Released eBook.
Remarks about the title: I know that is difficult to design a cover with a number. You can add the word TOP (in caps or not) before 47 blunders. It is not mandatory to insert the word TOP. It is up to you if you think you can create a better cover.
Subtitle is: A Newcomer's Manual for Releasing Solo, Shaping Pictures and Words, Arranging Pages, Boosting Sign-ups and Moving More Copies
Author: Dennis R. Albrook
Publisher: Lanternfield Works
The book made the presentation of errors that can occur during the production of an ebook. Title must be big, the title should be readable even when the image is reduced in size. No photo please.
I join my projects as an example. Do what you want but I need impact.

Target Market(s)

Book to sell first at Brisco Leafreader Shop. Target is authors, men or women, who want to produce ebooks.

Industry/Entity Type

Publishing Company

Font styles to use
Sans Serif

Colors
3176b5
9bcb3c

Requirements
Must have
• High readability when cover is small.
• Here is the definition of the word KILL
• put an end to or cause the failure or defeat of (something).
• "the committee voted to kill the project"
• synonyms: destroy, put an end to, end, extinguish, dash, quash, ruin, wreck, shatter, smash, crush, scotch, thwart; informalput the kibosh on, stymie, scuttle
• "this would kill all hopes of progress"
• veto, defeat, vote down, rule against, reject, throw out, overrule, overturn, put a stop to, quash, squash
• "an opposition attempt to kill the bill"
Nice to have
• I suggested 2 colors but you can you use another one or two. I want cover that sell. There is so bright ideas here. Come on down!
Should not have
• No picture or photo. If a photo or an object had power to the cover, you can insert one. I don't want a photo-collage.

```html
<!DOCTYPE html>
<html lang="en">
<head>
<meta charset="utf-8">
<title>47 Blunders That Sink Your Indie-Released eBook</title>
<link href="https://fonts.googleapis.com/css2?family=Anton&family=EB+Garamond:wght@600;700;800&display=swap" rel="stylesheet">
<style>
  :root {
    --blue: #3176b5;
    --blue-bevel-top: #8fb4dc;
    --blue-bevel-left: #2b64a0;
    --blue-shadow: #1f4a78;
    --green: #9bcb3c;
    --green-edge: #2f4d10;
    --ink: #0d0d0d;
    --paper: #ffffff;
    --burst-edge: #e8232f;
  }
  html, body {
    margin: 0;
    padding: 0;
    width: 927px;
    height: 1200px;
    overflow: hidden;
    background: var(--paper);
  }
  .cover {
    position: relative;
    width: 900px;
    height: 1165px;
    transform: scale(1.03);
    transform-origin: 0 0;
    background: var(--paper);
    overflow: hidden;
  }
  .cover-backdrop {
    position: absolute;
    inset: 0;
    width: 900px;
    height: 1165px;
  }
  .title {
    position: absolute;
    left: 140px;
    top: 28px;
    width: 640px;
    margin: 0;
    text-align: center;
    font-family: "Anton", "Impact", sans-serif;
    font-weight: 400;
  }
  .title-number,
  .title-word {
    display: block;
    color: var(--green);
    -webkit-text-stroke: 3px var(--green-edge);
    paint-order: stroke fill;
    text-shadow: 4px 6px 8px rgba(0, 0, 0, 0.55);
  }
  .title-number {
    font-size: 250px;
    line-height: 250px;
    letter-spacing: 12px;
  }
  .title-word {
    font-size: 122px;
    line-height: 128px;
    margin-top: -6px;
    letter-spacing: 1px;
  }
  .title-tail {
    display: block;
    color: var(--ink);
    font-size: 64px;
    line-height: 74px;
    margin-top: 6px;
    text-shadow: -2px -2px 0 var(--paper), 2px -2px 0 var(--paper), -2px 2px 0 var(--paper), 2px 2px 0 var(--paper), 0 3px 0 var(--paper);
  }
  .subtitle {
    position: absolute;
    left: 97px;
    top: 760px;
    margin: 0;
    font-family: "EB Garamond", "Garamond", serif;
    font-weight: 700;
    font-size: 31px;
    line-height: 46px;
    color: var(--ink);
    text-shadow: -1px -1px 0 var(--paper), 1px -1px 0 var(--paper), -1px 1px 0 var(--paper), 1px 1px 0 var(--paper);
  }
  .subtitle span { display: block; }
  .burst-text {
    position: absolute;
    left: 500px;
    top: 790px;
    width: 280px;
    text-align: center;
    font-family: "EB Garamond", "Garamond", serif;
    font-weight: 700;
    color: var(--ink);
  }
  .burst-text .lead { display: block; font-size: 32px; line-height: 34px; }
  .burst-text .punch { display: block; font-size: 54px; line-height: 56px; color: var(--green); font-weight: 800; }
  .burst-text .tail { display: block; font-size: 28px; line-height: 32px; }
  .author,
  .publisher {
    position: absolute;
    margin: 0;
    font-family: "Anton", "Impact", sans-serif;
    font-weight: 400;
    color: var(--ink);
    font-size: 32px;
    line-height: 40px;
  }
  .author { left: 70px; top: 1052px; }
  .publisher { right: 62px; top: 1056px; }
</style>
</head>
<body>
  <main class="cover">
    <svg class="cover-backdrop" viewBox="0 0 900 1165" aria-hidden="true">
      <polygon class="bevel-top" points="0,0 900,0 860,40 40,40" fill="var(--blue-bevel-top)"/>
      <polygon class="bevel-left" points="0,0 40,40 40,1000 0,1055" fill="var(--blue-bevel-left)"/>
      <polygon class="panel-blue" points="40,40 860,40 40,1000" fill="var(--blue)"/>
      <polygon class="panel-shadow" points="860,40 900,0 0,1055 40,1000" fill="var(--blue-shadow)"/>
      <polygon class="starburst" fill="var(--blue)" stroke="var(--burst-edge)" stroke-width="3" stroke-linejoin="miter"
        points="815,870 732,895 792,958 707,937 728,1022 665,962 640,1045 615,962 552,1022 573,937 488,958 548,895 465,870 548,845 488,782 573,803 552,718 615,778 640,695 665,778 728,718 707,803 792,782 732,845"/>
    </svg>

    <h1 class="title">
      <span class="title-number">47</span>
      <span class="title-word">Blunders</span>
      <span class="title-tail">That Sink Your<br>Indie-Released<br>eBook</span>
    </h1>

    <p class="subtitle">
      <span>A Newcomer's Manual for</span>
      <span>Releasing Solo,</span>
      <span>Shaping Pictures and Words,</span>
      <span>Arranging Pages,</span>
      <span>Boosting Sign-ups</span>
    </p>

    <p class="burst-text">
      <span class="lead">and</span>
      <span class="punch">Moving</span>
      <span class="tail">More Copies</span>
    </p>

    <p class="author">Dennis R. Albrook</p>
    <p class="publisher">Lanternfield Works</p>
  </main>
</body>
</html>
```